Halvorsen Winery Wine Label Re-design

Halvorsen Winery is located in the Finger Lakes region of New York. The Halvorsen Family planted the first vineyards in 1979 and opened in 1986. We produce award winning premium, hand crafted estate grown wines. We are in the process of a wine label re-design across our entire line. We would like to have the new label 'pop' but still convey elegance and ultra-premium quality. We are open to all color and styles or a minimalist design.
The attached files contain our new logo and samples of our current label (marked current) with dimensions. Our labeler is limited to label shapes but does not necessarily to have to be die-cut(the top arch) like our current label.

Target Market(s)

Upper income quality wine drinkers

Colors

Designer to choose colors to be used in the design.

Requirements
Should not have
• Should not be a tranparent label

```html
<!DOCTYPE html>
<html lang="en">
<head>
<meta charset="utf-8">
<title>Halvorsen Winery – Wine Labels</title>
<link rel="stylesheet" href="https://fonts.googleapis.com/css2?family=Cinzel:wght@400;600&family=Libre+Baskerville:wght@400;700&family=Raleway:wght@300&display=swap">
<style>
  :root {
    --backdrop: #f6f6f5;
    --paper: #f7f5f0;
    --plum: #4a1333;
    --shiraz: #c8111f;
    --shiraz-deep: #9e0d1c;
    --chardonnay: #56a98a;
    --chardonnay-deep: #3f8f72;
    --white: #ffffff;
  }
  * { box-sizing: border-box; margin: 0; padding: 0; }
  html, body {
    width: 1200px; height: 1200px; overflow: hidden;
    background: var(--backdrop);
  }
  .label-set {
    position: relative; width: 1200px; height: 1200px;
  }
  .label {
    position: absolute; top: 340px; width: 476px;
    background: var(--paper);
    box-shadow: 0 6px 18px rgba(0,0,0,0.08);
  }
  .label--shiraz { left: 90px; --accent: var(--shiraz); }
  .label--chardonnay { left: 634px; --accent: var(--chardonnay); }

  .label-arch {
    position: absolute; left: 50%; top: -40px; width: 110px; height: 110px;
    margin-left: -55px; border-radius: 50%;
    background: var(--paper); z-index: 2;
    display: flex; align-items: center; justify-content: center;
  }
  .label-arch-ring {
    width: 80px; height: 80px; border-radius: 50%;
    border: 3px solid var(--plum);
  }

  .label-head {
    position: relative; height: 232px;
    text-align: center;
  }
  .label-frame {
    position: absolute; inset: 6px 6px 0 6px;
    border: 2px solid var(--accent); border-bottom: none;
  }
  .brand-name {
    position: relative; z-index: 3;
    padding-top: 110px;
    font-family: "Cinzel", serif; font-weight: 400;
    font-size: 46px; line-height: 1; letter-spacing: 0.16em;
    color: var(--plum); margin-right: -0.16em;
  }
  .brand-sub {
    position: relative; z-index: 3; margin-top: 4px;
    font-family: "Raleway", sans-serif; font-weight: 300;
    font-size: 26px; letter-spacing: 0.55em; margin-right: -0.55em;
    color: var(--plum);
  }

  .label-art {
    position: relative; height: 161px;
  }
  .label--shiraz .label-art {
    background: linear-gradient(172deg, #c9283f 0%, #e6566d 30%, #d11d35 55%, #a60e22 80%, #7b0d1c 100%);
  }
  .label--chardonnay .label-art {
    background: linear-gradient(180deg, #9cc6cf 0%, #c6dcc9 30%, #a9c45e 60%, #7ea14c 80%, #4d7a5a 100%);
  }
  .label-tagline {
    position: absolute; top: 18px; left: 0; right: 0; text-align: center;
    font-family: "Libre Baskerville", serif; font-size: 12px;
    letter-spacing: 0.04em; color: var(--white);
  }
  .label--chardonnay .label-tagline { color: var(--plum); }

  .label-vintage {
    position: relative; height: 78px;
    display: flex; flex-direction: column; align-items: center; justify-content: center;
    font-family: "Libre Baskerville", serif; font-weight: 700;
    color: var(--plum);
  }
  .label-vintage .label-frame {
    inset: 0 6px 6px 6px; border: 2px solid var(--accent); border-top: none;
  }
  .vintage-year { font-size: 19px; letter-spacing: 0.14em; }
  .vintage-tier { font-size: 19px; letter-spacing: 0.42em; margin-right: -0.42em; line-height: 1.3; }

  .label-band {
    height: 58px; background: var(--accent);
    display: flex; align-items: center; justify-content: center;
    font-family: "Cinzel", serif; font-weight: 600; font-size: 25px;
    letter-spacing: 0.06em; color: var(--white);
  }
</style>
</head>
<body>
<main class="label-set">

  <article class="label label--shiraz">
    <div class="label-arch"><div class="label-arch-ring"></div></div>
    <header class="label-head">
      <div class="label-frame"></div>
      <p class="brand-name">HALVORSEN</p>
      <p class="brand-sub">WINERY</p>
    </header>
    <div class="label-art" role="img" aria-label="Red watercolour landscape with sky, hills and a tree">
      <p class="label-tagline">ESTATE GROWN &amp; BOTTLED</p>
    </div>
    <div class="label-vintage">
      <div class="label-frame"></div>
      <span class="vintage-year">2013</span>
    </div>
    <div class="label-band">SHIRAZ</div>
  </article>

  <article class="label label--chardonnay">
    <div class="label-arch"><div class="label-arch-ring"></div></div>
    <header class="label-head">
      <div class="label-frame"></div>
      <p class="brand-name">HALVORSEN</p>
      <p class="brand-sub">WINERY</p>
    </header>
    <div class="label-art" role="img" aria-label="Green and blue watercolour landscape with sky, meadow and a tree">
      <p class="label-tagline">ESTATE GROWN &amp; BOTTLED</p>
    </div>
    <div class="label-vintage">
      <div class="label-frame"></div>
      <span class="vintage-tier">RESERVE</span>
      <span class="vintage-year">2014</span>
    </div>
    <div class="label-band">CHARDONNAY</div>
  </article>

</main>
</body>
</html>
```